Retractable Banner design

We need to a banner design to print on a retractable banner of size 31.5"W X 95.85" H. This banner will be displayed at the universities seminars conducted during campus recruitment process. Audience will be masters gradutes with IT or non-IT background.

Please use images which are suitable for the cause, and also words which emphasize the bright future and jobs. You can come up with suitable colors or using the logo colors. Sample banner, which we used before is attached. Need some attractive designs.

Some of the Text which has to be displaed apart from the images :

For the fresh graduates (OPT/CPT) , Brightpath Works is a learning ground, an opportunity for growth, a stepping stone in the career graph and a substantial elevator for an excellent future.

BENEFITS:

Free Training (CPT / OPT Students) and Free Accomodationm
Project Based Training
Well Experienced faculty working in real time environments
Exposure to Real Time Application, 24/7 access to labs
Free H1-B Processing for eligible OPT students
100% Placement assured
Efficient sales and marketing team, Competetive salary
Zero Cost to you, until you receive your first paycheck

http://www.brightpathworksco.example

42 Willowmere Ave, Ste 610, Danbury, CT 06810
Tel: (555)314-2096 Ext : 418

info@brightpathworksco.example

Target Market(s)

Masters graduates applying for Jobs

Industry/Entity Type

University

Colors

Designer to choose colors to be used in the design.

```html
<!DOCTYPE html>
<html lang="en">
<head>
<meta charset="utf-8">
<title>Brightpath Works – Retractable Banner</title>
<link rel="stylesheet" href="https://fonts.googleapis.com/css2?family=Oswald:wght@500;600&family=Lato:wght@400;700;900&family=Jost:wght@300;400;500&display=swap">
<style>
  :root{
    --stage:#2b2b2d;
    --blue:#1467b8;
    --blue-dark:#0d4f96;
    --blue-light:#3f8fd2;
    --green:#8cc63f;
    --green-dark:#5e9e2a;
    --orange:#f7941d;
    --orange-dark:#e36a1e;
    --orange-light:#f6a83e;
    --ink:#333;
    --white:#fff;
  }
  *{box-sizing:border-box;margin:0;padding:0}
  html,body{width:960px;height:1200px;overflow:hidden;background:var(--stage)}
  .board{position:relative;width:960px;height:1200px}
  .banner{position:absolute;top:41px;width:348px;height:1053px;background:var(--white);overflow:hidden;font-family:"Lato",sans-serif}
  .banner--one{left:97px;--panel-a:var(--orange-light);--panel-b:#e38a26;--tab:var(--orange-dark);--footer:var(--blue);--v-main:var(--blue);--v-side:var(--blue-dark);--v-tip:var(--green);--photo-a:#c9b8a4;--photo-b:#6b6f7a}
  .banner--two{left:504px;--panel-a:#3d8ed3;--panel-b:#1d63ab;--tab:#1d3f78;--footer:var(--orange);--v-main:var(--green);--v-side:var(--green-dark);--v-tip:var(--orange);--photo-a:#a9b89a;--photo-b:#5d6a78}

  .photo{position:absolute;left:0;top:0;width:100%;height:360px;
    background:linear-gradient(180deg,#fff 0%,#fff 10%,var(--photo-a) 35%,var(--photo-b) 100%)}
  .brand{position:absolute;top:40px;left:0;width:100%;display:flex;justify-content:center;align-items:center;gap:7px}
  .brand__dot{width:20px;height:20px;border-radius:50%;background:var(--blue)}
  .brand__name{font-family:"Lato",sans-serif;font-weight:900;font-size:21px;color:var(--blue)}
  .chevron{position:absolute;left:0;top:230px;width:348px;height:150px}

  .intro{position:absolute;left:15px;top:364px;right:10px;color:var(--ink)}
  .intro__lead{font-family:"Jost",sans-serif;font-size:19px;font-weight:400;letter-spacing:.3px}
  .intro__title{font-family:"Oswald",sans-serif;font-weight:600;font-size:26px;color:var(--orange);line-height:1.25;letter-spacing:.2px}
  .pitch{position:absolute;left:17px;top:423px;right:6px;height:130px;display:flex;gap:9px}
  .pitch__tag{width:28px;background:var(--green);color:#fff;writing-mode:vertical-rl;transform:rotate(180deg);
    font-weight:900;font-size:10.5px;letter-spacing:.6px;text-align:center;padding:4px 0}
  .pitch__list{list-style:none;font-size:14.5px;line-height:1.15;color:var(--ink);display:flex;flex-direction:column;justify-content:space-between;padding:6px 0 4px}

  .benefits{position:absolute;left:0;top:558px;width:100%;height:373px;
    background:linear-gradient(160deg,var(--panel-a),var(--panel-b));color:#fff;text-align:center;padding:0 34px}
  .benefits__tab{display:inline-block;background:var(--tab);border-radius:0 0 8px 8px;padding:6px 14px 3px;
    font-family:"Lato",sans-serif;font-weight:900;font-size:21px;letter-spacing:.5px}
  .benefits__list{list-style:none;margin-top:6px}
  .benefit{font-size:12.4px;text-transform:uppercase;line-height:1.3;padding:5px 0;border-bottom:1px solid rgba(255,255,255,.3);letter-spacing:.2px}
  .benefit:last-child{border-bottom:0}
  .benefit--big{display:flex;align-items:center;justify-content:center;gap:5px;text-align:left;padding:3px 0}
  .benefit__em{font-family:"Oswald",sans-serif;font-weight:600;font-size:35px;line-height:1}
  .benefit__pct{font-family:"Lato",sans-serif;font-weight:900;font-size:22px;line-height:1}

  .contact{position:absolute;left:0;top:931px;width:100%;text-align:center}
  .contact__address{font-family:"Jost",sans-serif;font-weight:400;font-size:14px;line-height:1.3;color:var(--ink);margin-top:6px}
  .contact__phone{font-family:"Lato",sans-serif;font-weight:900;font-size:22px;color:var(--green);margin-top:4px}
  .contact__ext{font-family:"Jost",sans-serif;font-weight:500;font-size:16px}
  .web{position:absolute;left:0;bottom:0;width:100%;height:38px;background:var(--footer);color:#fff;
    display:flex;align-items:center;justify-content:center;font-size:14.5px;letter-spacing:.2px}
  .web strong{font-weight:900}

  .label{position:absolute;top:1118px;width:348px;text-align:center;font-family:"Lato",sans-serif;font-size:26px;color:#e6e6e6}
  .label--one{left:97px}.label--two{left:504px}
</style>
</head>
<body>
<main class="board">

  <article class="banner banner--one">
    <div class="photo" role="img" aria-label="Photo of four smiling graduate students walking together with books"></div>
    <div class="brand"><span class="brand__dot"></span><span class="brand__name">Brightpath Works</span></div>
    <svg class="chevron" viewBox="0 0 348 150" aria-hidden="true">
      <polygon points="0,30 190,118 348,40 348,80 190,150 0,95" fill="var(--v-main)"/>
      <polygon points="190,118 348,40 348,68" fill="var(--v-side)"/>
      <polygon points="0,95 190,150 348,80 348,150 0,150" fill="#fff"/>
      <polygon points="220,137 348,80 348,120" fill="var(--v-tip)"/>
    </svg>
    <header class="intro">
      <p class="intro__lead">FOR THE</p>
      <h1 class="intro__title">FRESH GRADUATES (OPT/CPT)</h1>
    </header>
    <section class="pitch">
      <div class="pitch__tag">BRIGHTPATH WORKS IS</div>
      <ul class="pitch__list">
        <li>A LEARNING GROUND,</li>
        <li>AN OPPORTUNITY FOR GROWTH,</li>
        <li>A STEPPING STONE IN THE CAREER GRAPH AND A SUBSTANTIAL ELEVATOR FOR AN EXCELLENT FUTURE.</li>
      </ul>
    </section>
    <section class="benefits">
      <h2 class="benefits__tab">BENEFITS:</h2>
      <ul class="benefits__list">
        <li class="benefit benefit--big"><span class="benefit__em">FREE</span><span>Training (CPT / OPT students) &amp;<br>Accomodationm</span></li>
        <li class="benefit">Project based training</li>
        <li class="benefit">Well experienced faculty working in<br>real time environments</li>
        <li class="benefit">Exposure to real time application,<br>24/7 access to labs</li>
        <li class="benefit benefit--big"><span class="benefit__em">FREE</span><span>H1-B processing for<br>eligible OPT students</span></li>
        <li class="benefit benefit--big"><span class="benefit__pct">100%</span><span>Placement assured</span></li>
        <li class="benefit">Efficient sales and marketing team,<br>competetive salary</li>
        <li class="benefit">Zero cost to you,<br>until you receive your first paycheck</li>
      </ul>
    </section>
    <footer class="contact">
      <p class="contact__address">42 Willowmere Ave, Ste 610,<br>Danbury, CT 06810</p>
      <p class="contact__phone">(555)314-2096 <span class="contact__ext">Ext : 418</span></p>
    </footer>
    <div class="web">WWW.<strong>BRIGHTPATHWORKSCO</strong>.EXAMPLE</div>
  </article>

  <article class="banner banner--two">
    <div class="photo" role="img" aria-label="Photo of five students sitting together outdoors reading a book and tablet"></div>
    <div class="brand"><span class="brand__dot"></span><span class="brand__name">Brightpath Works</span></div>
    <svg class="chevron" viewBox="0 0 348 150" aria-hidden="true">
      <polygon points="0,30 190,118 348,40 348,80 190,150 0,95" fill="var(--v-main)"/>
      <polygon points="190,118 348,40 348,68" fill="var(--v-side)"/>
      <polygon points="0,95 190,150 348,80 348,150 0,150" fill="#fff"/>
      <polygon points="220,137 348,80 348,120" fill="var(--v-tip)"/>
    </svg>
    <header class="intro">
      <p class="intro__lead">FOR THE</p>
      <h1 class="intro__title">FRESH GRADUATES (OPT/CPT)</h1>
    </header>
    <section class="pitch">
      <div class="pitch__tag">BRIGHTPATH WORKS IS</div>
      <ul class="pitch__list">
        <li>A LEARNING GROUND,</li>
        <li>AN OPPORTUNITY FOR GROWTH,</li>
        <li>A STEPPING STONE IN THE CAREER GRAPH AND A SUBSTANTIAL ELEVATOR FOR AN EXCELLENT FUTURE.</li>
      </ul>
    </section>
    <section class="benefits">
      <h2 class="benefits__tab">BENEFITS:</h2>
      <ul class="benefits__list">
        <li class="benefit benefit--big"><span class="benefit__em">FREE</span><span>Training (CPT / OPT students) &amp;<br>Accomodationm</span></li>
        <li class="benefit">Project based training</li>
        <li class="benefit">Well experienced faculty working in<br>real time environments</li>
        <li class="benefit">Exposure to real time application,<br>24/7 access to labs</li>
        <li class="benefit benefit--big"><span class="benefit__em">FREE</span><span>H1-B processing for<br>eligible OPT students</span></li>
        <li class="benefit benefit--big"><span class="benefit__pct">100%</span><span>Placement assured</span></li>
        <li class="benefit">Efficient sales and marketing team,<br>competetive salary</li>
        <li class="benefit">Zero cost to you,<br>until you receive your first paycheck</li>
      </ul>
    </section>
    <footer class="contact">
      <p class="contact__address">42 Willowmere Ave, Ste 610,<br>Danbury, CT 06810</p>
      <p class="contact__phone">(555)314-2096 <span class="contact__ext">Ext : 418</span></p>
    </footer>
    <div class="web">WWW.<strong>BRIGHTPATHWORKSCO</strong>.EXAMPLE</div>
  </article>

  <p class="label label--one">Version 1</p>
  <p class="label label--two">Version 2</p>
</main>
</body>
</html>
```